Letterhead for small civil engineer company

We need bold and modern design for company letterhead in MS word. It needs to have company logo and company info. Somewhere in the upper right part of document needs to be space for "recever" and the documents starts with, example, "SUBJECT: CIVIL ENGINEER LETTERHEAD".

in the bottom part of document needs to be signature and date.

Company info: Veltrana d.o.o., Lipovac 18, Lipovac (Općina Brestina), OIB 47396025814, www.veltrana.hr, info@veltrana.hr

Email of document sender needs to be somewhere if document, exapmle xyz@veltran.hr

Target Market(s)

Civil engineer company and projects

Industry/Entity Type

Civil engineer

Font styles to use
Serif

Colors
F0912C
F2A743
F7CA91
FBE8D2
FDF5EE

Requirements
Must have
• Company logo and company info
Nice to have
• Moder and clean design
Should not have
• Too much details

```html
<!DOCTYPE html>
<html lang="en">
<head>
<meta charset="utf-8">
<title>Veltrana Letterhead</title>
<link href="https://fonts.googleapis.com/css2?family=DM+Sans:wght@400;500;600;700&display=swap" rel="stylesheet">
<style>
  :root {
    --orange: #E68A2B;
    --ink: #666666;
    --ink-soft: #6f6f6f;
    --paper: #ffffff;
    --backdrop: #e9e9e9;
    --sig-tint: #FBE8D2;
  }
  * { margin: 0; padding: 0; box-sizing: border-box; }
  html, body { width: 1200px; height: 1200px; overflow: hidden; }
  body {
    background: var(--backdrop);
    font-family: "DM Sans", sans-serif;
    color: var(--ink);
    position: relative;
  }
  .letterhead {
    position: absolute;
    left: 270px; top: 133px;
    width: 660px; height: 934px;
    background: var(--paper);
    overflow: hidden;
  }
  .top-accent {
    position: absolute; left: 68px; top: 0;
    width: 146px; height: 5px; background: var(--orange);
  }
  .brand {
    position: absolute; left: 68px; top: 50px; width: 146px;
    text-align: center;
  }
  .brand-square {
    width: 52px; height: 52px; margin: 0 auto;
    border: 2px solid var(--ink);
  }
  .brand-name {
    margin-top: 6px;
    font-size: 20px; font-weight: 500; letter-spacing: 0.5px;
    color: var(--orange); line-height: 1;
  }
  .tax-id {
    position: absolute; right: 54px; top: 67px;
    font-size: 13.5px; font-weight: 700; color: var(--ink);
  }
  .rule-orange {
    position: absolute; left: 242px; top: 86px;
    width: 367px; height: 2px; background: var(--orange);
  }
  .rule-grey {
    position: absolute; left: 609px; top: 87px;
    width: 51px; height: 1px; background: #888;
  }
  .recipient {
    position: absolute; left: 68px; top: 203px;
    font-size: 11px; font-weight: 600; line-height: 18px;
    text-transform: uppercase;
  }
  .recipient .company { color: var(--orange); }
  .subject {
    position: absolute; left: 68px; top: 284px;
    font-size: 14.5px; font-weight: 700; color: var(--ink);
  }
  .body {
    position: absolute; left: 68px; top: 316px; width: 507px;
    font-size: 11px; line-height: 17.8px; color: var(--ink-soft);
    text-align: justify;
  }
  .body p + p { margin-top: 15px; }
  .signature-mark {
    position: absolute; left: 68px; top: 602px;
  }
  .sign-name {
    position: absolute; left: 68px; top: 656px;
    font-size: 11px; font-weight: 700;
  }
  .sign-date {
    position: absolute; left: 68px; top: 680px;
    font-size: 8.5px;
  }
  .footer-item {
    position: absolute; top: 868px;
    font-size: 11px; line-height: 18px; color: var(--ink-soft);
    display: flex; align-items: center;
  }
  .footer-item svg { flex: none; }
  .footer-address { left: 62px; }
  .footer-address svg { margin-right: 8px; }
  .footer-web { left: 268px; }
  .footer-web svg { margin-right: 5px; }
  .footer-mail { left: 443px; }
  .footer-mail svg { margin-right: 9px; }
  .corner {
    position: absolute; left: 0; top: 0;
  }
</style>
</head>
<body>
  <main class="letterhead">
    <div class="top-accent"></div>

    <div class="brand">
      <div class="brand-square"></div>
      <div class="brand-name">VELTRANA</div>
    </div>

    <div class="tax-id">OIB 47396025814</div>
    <div class="rule-orange"></div>
    <div class="rule-grey"></div>

    <div class="recipient">
      <div>To</div>
      <div>Recipient Name</div>
      <div class="company">Veltrana</div>
    </div>

    <h1 class="subject">SUBJECT: CIVIL ENGINEER LETTERHEAD</h1>

    <div class="body">
      <p>Lorem ipsum dolor sit amet, consectetuer adipiscing elit, sed diam nonummy nibh euismod tinci&shy;dunt ut laoreet dolore magna aliquam erat volutpat. Ut wisi enim ad minim</p>
      <p>Lorem ipsum dolor sit amet, consectetuer adipiscing elit, sed diam nonummy nibh euismod tinci&shy;dunt ut laoreet dolore magna aliquam erat volutpat. Ut wisi enim ad minim veniam, quis nostrud exerci tation ullamcorper suscipit lobortis nisl ut aliquip ex ea commodo consequat. Duis autem vel eum iriure dolor in hendrerit in vulputate velit esse molestie consequat, vel illum dolore eu feugiat nulla facilisis at vero eros et accumsan</p>
      <p style="margin-top:22px">Lorem ipsum dolor sit amet, consectetuer adipiscing elit, sed diam nonummy nibh euismod tinci&shy;dunt ut laoreet dolore magna aliquam erat volutpat. Ut wisi enim ad minim veniam, quis nostrud exerci tation ullamcorper suscipit lobortis nisl ut aliquip ex ea commodo consequat. Duis autem vel eum iriure dolor in hendrerit in vulputate velit esse molestie consequat, vel illum dolore eu feugiat nulla facilisis at vero eros et accumsan et iusto odio dignissim qui blandit praesent luptatum zzril delenit augue duis dolore te</p>
    </div>

    <svg class="signature-mark" width="114" height="38" role="img" aria-label="Handwritten signature">
      <rect width="114" height="38" rx="4" fill="var(--sig-tint)"/>
    </svg>
    <div class="sign-name">Your Signature Name</div>
    <div class="sign-date">12/13/24</div>

    <div class="footer-item footer-address">
      <svg width="17" height="22" viewBox="0 0 17 22" fill="none" stroke="var(--orange)" stroke-width="1.6">
        <path d="M8.5 21C8.5 21 1.5 12.5 1.5 8A7 7 0 0 1 15.5 8C15.5 12.5 8.5 21 8.5 21Z"/>
        <circle cx="8.5" cy="8" r="2.6"/>
      </svg>
      <div>Veltrana d.o.o., Lipovac 18,<br>Lipovac (Općina Brestina)</div>
    </div>

    <div class="footer-item footer-web">
      <svg width="23" height="23" viewBox="0 0 23 23" fill="none" stroke="var(--orange)" stroke-width="1.5">
        <circle cx="11.5" cy="11.5" r="10"/>
        <ellipse cx="11.5" cy="11.5" rx="4.5" ry="10"/>
        <path d="M1.5 11.5H21.5M3 6.5H20M3 16.5H20"/>
      </svg>
      <div>www.veltrana.hr</div>
    </div>

    <div class="footer-item footer-mail">
      <svg width="24" height="22" viewBox="0 0 24 22" fill="none" stroke="var(--orange)" stroke-width="1.6" stroke-linejoin="round">
        <path d="M22.5 1.5L1.5 9.5L10 12L13 20.5Z"/>
        <path d="M10 12L22.5 1.5"/>
      </svg>
      <div>xyz@veltran.hr<br>info@veltrana.hr</div>
    </div>

    <svg class="corner" width="660" height="934" viewBox="0 0 660 934">
      <polygon points="595,880 660,880 660,934 564,934" fill="var(--orange)"/>
      <rect x="0" y="930" width="660" height="4" fill="var(--orange)"/>
    </svg>
  </main>
</body>
</html>
```